Bright Meadow Dental - Stationary
Business Cards, Letterhead, & Envelope
Project: Bright Meadow Dental - Stationary
Bright Meadow Dental - Stationary - Health
Creative Brief
Professional
Leland Fisk, D.D.S.
3847 W Thornbury Ln, Suite 2 Gladstone, MO 64102
BrightMeadowDental@mailbox-example.com
www.BrightMeadowDental-example.com
We're a fun office and want people to expect great cosmetic work and accommodations for families. We don't need a "blow your mind" presentation, just something classy.

```html
<!DOCTYPE html>
<html lang="en">
<head>
<meta charset="utf-8">
<title>Bright Meadow Dental – Stationery</title>
<link href="https://fonts.googleapis.com/css2?family=Cormorant+Garamond:wght@500&family=Open+Sans:wght@400;600&display=swap" rel="stylesheet">
<style>
  :root {
    --stage: #a7a8aa;
    --paper: #ffffff;
    --paper-edge: #d9dadb;
    --brand-blue: #2f7fb3;
    --ink: #4a4d52;
    --ink-soft: #7b7f85;
  }
  * { box-sizing: border-box; margin: 0; padding: 0; }
  html, body { width: 1200px; height: 684px; overflow: hidden; }
  body {
    background: var(--stage);
    font-family: "Open Sans", Arial, sans-serif;
    color: var(--ink);
    position: relative;
  }
  .sheet {
    position: absolute;
    background: var(--paper);
    box-shadow: 0 1px 3px rgba(0,0,0,.25);
  }
  .wordmark {
    font-family: "Cormorant Garamond", "Times New Roman", serif;
    font-weight: 500;
    color: var(--brand-blue);
    letter-spacing: .04em;
    text-transform: uppercase;
    line-height: 1.05;
    display: flex;
    align-items: center;
    gap: 6px;
    white-space: nowrap;
  }
  .wordmark .dot {
    width: 8px; height: 8px; border-radius: 50%;
    background: var(--brand-blue); flex: none;
  }
  .tagline {
    font-size: 6px; color: var(--ink-soft); letter-spacing: .05em; margin-top: 3px;
  }
  .contact-list { list-style: none; font-size: 6px; line-height: 9px; color: var(--ink); }
  .contact-list li { display: flex; align-items: center; gap: 4px; white-space: nowrap; }
  .contact-list li::before {
    content: ""; width: 4px; height: 4px; background: var(--ink); border-radius: 1px; flex: none;
  }

  /* Letterhead */
  .letterhead { left: 180px; top: 19px; width: 408px; height: 658px; }
  .letterhead .brand { position: absolute; left: 28px; top: 62px; }
  .letterhead .wordmark { font-size: 18px; }
  .letterhead .contact-list { position: absolute; left: 28px; bottom: 24px; }

  /* Business card */
  .business-card { left: 24px; top: 305px; width: 161px; height: 89px; }
  .business-card .brand { position: absolute; left: 10px; top: 11px; }
  .business-card .wordmark { font-size: 10px; gap: 4px; }
  .business-card .wordmark .dot { width: 5px; height: 5px; }
  .business-card .tagline { font-size: 4.5px; }
  .business-card .contact-list { position: absolute; left: 10px; top: 40px; font-size: 4.2px; line-height: 6.5px; }
  .business-card .contact-list li { gap: 3px; }
  .business-card .contact-list li::before { width: 3px; height: 3px; }
  .business-card .person { position: absolute; right: 10px; bottom: 5px; font-size: 4.5px; color: var(--ink); }

  /* Envelope back */
  .envelope-back { left: 629px; top: 36px; width: 547px; height: 240px; }
  .envelope-back svg { position: absolute; inset: 0; }
  .envelope-back .flap-mark {
    position: absolute; left: 0; right: 0; top: 54px;
    text-align: center; font-family: "Cormorant Garamond", "Times New Roman", serif;
    font-weight: 500; font-size: 10px; letter-spacing: .06em; text-transform: uppercase; color: var(--brand-blue);
  }

  /* Envelope front */
  .envelope-front { left: 629px; top: 379px; width: 547px; height: 269px; }
  .envelope-front .brand { position: absolute; left: 28px; top: 90px; }
  .envelope-front .wordmark { font-size: 14px; }
  .envelope-front .contact-list { position: absolute; left: 28px; top: 170px; }
  .envelope-front .web { position: absolute; right: 20px; bottom: 34px; font-size: 6px; color: var(--ink); font-weight: 600; }
</style>
</head>
<body>

  <section class="sheet letterhead" aria-label="Letterhead">
    <div class="brand">
      <div class="wordmark"><span class="dot"></span>Bright Meadow Dental</div>
      <div class="tagline">Cosmetic and Family Dentistry</div>
    </div>
    <ul class="contact-list">
      <li>P: 555.201.0140</li>
      <li>F: 555.201.0141</li>
      <li>BrightMeadowDental@mailbox-example.com</li>
      <li>3847 W Thornbury Ln, Suite 2 Alder Falls 00000</li>
    </ul>
  </section>

  <section class="sheet business-card" aria-label="Business card">
    <div class="brand">
      <div class="wordmark"><span class="dot"></span>Bright Meadow Dental</div>
      <div class="tagline">Cosmetic and Family Dentistry</div>
    </div>
    <ul class="contact-list">
      <li>P: 555.201.0140</li>
      <li>F: 555.201.0141</li>
      <li>lfisk@mailbox-example.com</li>
      <li>3847 W Thornbury Ln, Suite 2 Alder Falls 00000</li>
      <li>www.BrightMeadowDental-example.com</li>
    </ul>
    <div class="person">Leland Fisk, D.D.S.</div>
  </section>

  <section class="sheet envelope-back" aria-label="Envelope back">
    <svg width="547" height="240" viewBox="0 0 547 240" aria-hidden="true">
      <path d="M0 2 C60 10 150 40 230 88 Q273 110 317 88 C397 40 487 10 547 2"
            fill="none" stroke="var(--paper-edge)" stroke-width="1.2"/>
    </svg>
    <div class="flap-mark">Bright Meadow Dental</div>
  </section>

  <section class="sheet envelope-front" aria-label="Envelope front">
    <div class="brand">
      <div class="wordmark"><span class="dot"></span>Bright Meadow Dental</div>
      <div class="tagline">Cosmetic and Family Dentistry</div>
    </div>
    <ul class="contact-list">
      <li>P: 555.201.0140</li>
      <li>F: 555.201.0141</li>
      <li>BrightMeadowDental@mailbox-example.com</li>
      <li>3847 W Thornbury Ln, Suite 2 Alder Falls 00000</li>
    </ul>
    <div class="web">www.BrightMeadowDental-example.com</div>
  </section>

</body>
</html>
```